Tess Marlowe Communication business card

I am starting a small, country-based business that offers writing, communication and marketing services to a wide range of clients, inner city big business, to mining, through to agriculture.

The appeal of my business is that it's mobile and flexible. It's just me, with lots of hands-on experience on construction and infrastructure projects.

I can provide the following services:

• Communication planning and management
• Issues and media management
• Marketing and communication materials
• Project management and strategy
• Government liaison
• Incident management communication
• Stakeholder management

It would be great to be able to use the elements of the business card design on other stationery.

Industry/Entity Type

Communication

Requirements
Must have
• The following information:

Tess Marlowe
M: 0427 391 864
E: tess@tmcommsmail.com

PO Box 152
Durrandale Q 4472
Nice to have
• a rural element (windmill, workboots, wheat stalk)

```html
<!DOCTYPE html>
<html lang="en">
<head>
<meta charset="utf-8">
<title>Tess Marlowe Communication – Business Card</title>
<link rel="stylesheet" href="https://fonts.googleapis.com/css2?family=Cinzel:wght@400;600;700&family=Open+Sans:wght@400&display=swap">
<style>
  :root {
    --backdrop: #ece8e1;
    --card-white: #ffffff;
    --wheat-gold: #f0bd35;
    --wheat-gold-deep: #e9b32a;
    --ink: #111111;
    --ink-soft: #3a3a3a;
  }
  * { margin: 0; padding: 0; box-sizing: border-box; }
  html, body {
    width: 1200px;
    height: 1200px;
    overflow: hidden;
    background: var(--backdrop);
  }
  .canvas {
    position: relative;
    width: 1200px;
    height: 1200px;
  }
  .card {
    position: absolute;
    left: 180px;
    width: 840px;
    height: 490px;
    overflow: hidden;
    box-shadow: 0 6px 18px rgba(0,0,0,0.12);
  }

  /* Front: contact side */
  .card-front {
    top: 90px;
    background: var(--card-white);
  }
  .card-front .swoosh {
    position: absolute;
    inset: 0;
    width: 100%;
    height: 100%;
  }
  .identity {
    position: absolute;
    right: 46px;
    top: 62px;
    text-align: right;
  }
  .identity .person-name {
    font-family: "Cinzel", serif;
    font-weight: 600;
    font-size: 40px;
    color: var(--ink);
    letter-spacing: 0.5px;
    line-height: 1;
  }
  .identity .person-role {
    font-family: "Open Sans", sans-serif;
    font-size: 17px;
    color: var(--ink-soft);
    margin-top: 4px;
    margin-right: 4px;
  }
  .contact {
    position: absolute;
    left: 0;
    right: 0;
    top: 190px;
    padding-left: 90px;
    text-align: center;
    font-family: "Cinzel", serif;
    font-weight: 600;
    color: var(--ink);
  }
  .contact .line-address {
    font-size: 30px;
    line-height: 1.15;
  }
  .contact .line-detail {
    font-size: 24px;
    line-height: 1.3;
    font-weight: 400;
  }

  /* Back: brand side */
  .card-back {
    top: 630px;
    background: var(--wheat-gold);
  }
  .brand-mark {
    position: absolute;
    left: 50%;
    top: 78px;
    width: 170px;
    height: 170px;
    margin-left: -85px;
    background: var(--ink);
    border-radius: 16px;
  }
  .brand-name {
    position: absolute;
    left: 0;
    right: 0;
    top: 300px;
    text-align: center;
    font-family: "Cinzel", serif;
    font-weight: 600;
    font-size: 40px;
    color: var(--ink);
    letter-spacing: 0.5px;
  }
</style>
</head>
<body>
  <main class="canvas">
    <section class="card card-front" aria-label="Business card, contact side">
      <svg class="swoosh" viewBox="0 0 840 490" preserveAspectRatio="none" aria-hidden="true">
        <path d="M390 0 C 520 70, 680 120, 840 128 L 840 182 C 660 176, 480 110, 350 0 Z" fill="var(--wheat-gold)"/>
      </svg>
      <div class="identity">
        <p class="person-name">Tess Marlowe</p>
        <p class="person-role">Ceo &amp; Founder</p>
      </div>
      <div class="contact">
        <p class="line-address">PO Box 152</p>
        <p class="line-address">Durrandale Q 4472</p>
        <p class="line-detail">M: 0427 391 864</p>
        <p class="line-detail">Email: tess@tmcommsmail.com</p>
      </div>
    </section>

    <section class="card card-back" aria-label="Business card, brand side">
      <div class="brand-mark" aria-hidden="true"></div>
      <p class="brand-name">Tess Marlowe Communication</p>
    </section>
  </main>
</body>
</html>
```